C U B A N - C I G A R S - F L Y E R

I need a double-sided 5x7 club type flyer for a Memorial Day Weekend Trip.
The main side design needs to be similar to the attached flyer example. The front design of flyer is KEY. The design will be awarded to the closest finished submission to the example flyer.
Both sides of the flyer should also included event and business logo, which are also attached. Both logos can be altered to fit printing need accordingly.
Front side content is also attached.
The back side design will be very simple. Consists of 3 travel images and trip description, and my contact very details. Same color design as front. The attached word document contains backside details for REFERENCE ONLY. Please focus on front side when submitting a design for this project.
Target Market(s)
A F R I C A N - A M E R I C A N - C I G A R - S M O K E R S
Industry/Entity Type
Travel Industry
Requirements
Must have
- All the elements of the attached information
Nice to have
- Masculine Images
Should not have
- Large Cigar focus to catch customer's attention

```html
<!DOCTYPE html>
<html lang="en">
<head>
<meta charset="utf-8">
<title>Cuba Cigar Gentlemen – Memorial Day Weekend Flyer</title>
<link rel="stylesheet" href="https://fonts.googleapis.com/css2?family=Oswald:wght@400;500;600&family=Yellowtail&family=Raleway:wght@400;500;600;700&family=Lato:wght@400;700&display=swap">
<style>
  :root{
    --stage:#6e6a2e;
    --pink:#ea8b8f;
    --sky:#7fa4d3;
    --navy:#24418a;
    --ink:#2a1f1b;
    --white:#ffffff;
    --smoke-dark:#1d1d1f;
    --smoke-mid:#4b4b4e;
    --back-brown:#4a3d36;
    --back-deep:#2e2420;
    --footer:#2a2220;
    --coral:#f07c7a;
    --blue-text:#7fb6ee;
    --rule:#cfc6c0;
  }
  *{box-sizing:border-box;margin:0;padding:0}
  html,body{width:1200px;height:844px;overflow:hidden;background:var(--stage)}
  .canvas{position:relative;width:1200px;height:844px}
  .card{position:absolute;transform-origin:top left;transform:scale(.8);overflow:hidden;box-shadow:0 6px 18px rgba(0,0,0,.35)}

  /* ---------- FRONT ---------- */
  .front{left:70px;top:286px;width:733px;height:524px;
    background:radial-gradient(ellipse at 30% 30%,var(--smoke-mid),var(--smoke-dark) 75%)}
  .front .hero-photo{position:absolute;left:0;top:0;width:458px;height:524px;
    background:radial-gradient(ellipse at 55% 45%,#8a7356 0%,#4a3a2c 35%,rgba(29,29,31,0) 70%)}
  .front .edge-photo{position:absolute;left:714px;top:0;width:19px;height:524px;background:#2a2a2c}
  .panel{position:absolute;left:458px;top:0;width:256px;height:524px;background:var(--sky)}
  .panel-inner{position:absolute;left:9px;top:0;width:236px;height:524px;background:var(--pink);
    text-align:center;font-family:"Raleway",sans-serif;color:var(--white)}
  .event-name{position:absolute;left:0;width:100%;top:30px;display:flex;flex-direction:column;align-items:center;gap:8px}
  .event-name .dot{width:16px;height:16px;border-radius:50%;background:var(--navy)}
  .event-name .name{font-family:"Raleway",sans-serif;font-weight:600;font-size:20px;line-height:24px;color:var(--navy)}
  .headline{position:absolute;left:0;width:100%;top:139px;font-family:"Oswald",sans-serif;font-weight:500;font-size:17px;line-height:24px;letter-spacing:.3px}
  .script{position:absolute;left:0;width:100%;top:160px;font-family:"Yellowtail",cursive;font-size:22px;line-height:26px;color:var(--navy)}
  .teaser{position:absolute;left:0;width:100%;top:191px;font-size:12.5px;line-height:16px;font-weight:500}
  .pitch{position:absolute;left:0;width:100%;top:222px;color:var(--ink);font-size:15px;line-height:18px}
  .pitch strong{font-weight:600}
  .dates-block{position:absolute;left:0;width:100%;top:340px;font-size:15.5px;line-height:19px;font-weight:600}
  .dates-block .label{color:var(--navy)}
  .band{position:absolute;left:-8px;width:270px;background:var(--sky);font-family:"Raleway",sans-serif}
  .band-year{top:289px;height:40px;display:flex;align-items:center;justify-content:center;gap:8px}
  .band-year .small{font-size:9.5px;line-height:12px;color:var(--navy);text-align:left;font-weight:500}
  .band-year .small b{font-size:12px;font-weight:600}
  .band-year .year{font-family:"Oswald",sans-serif;font-size:26px;color:var(--navy)}
  .band-book{top:437px;height:54px;text-align:center;padding-top:5px}
  .band-book .cta{font-size:17px;font-weight:700;color:var(--navy);line-height:20px}
  .band-book .sub{font-size:18px;color:var(--white);line-height:22px}
  .brand{position:absolute;left:23px;top:442px;width:76px;height:76px;border-radius:50%;border:2px solid var(--white);
    display:flex;align-items:center;justify-content:center;font-family:"Raleway",sans-serif;font-size:11px;font-weight:600;color:var(--white);text-align:center;line-height:13px}
  .contact-front{position:absolute;left:114px;top:458px;font-family:"Raleway",sans-serif;font-size:12.5px;line-height:22px;color:var(--coral)}
  .contact-front .url{color:var(--white);font-style:italic}
  .contact-front .phone{color:var(--white)}

  /* ---------- BACK ---------- */
  .back{left:682px;top:119px;width:523px;height:733px;background:var(--back-brown);font-family:"Lato",sans-serif;color:var(--white)}
  .photo{position:absolute;top:36px;width:144px;height:105px;border:1px solid #6b5a50}
  .photo.cars{left:36px;background:linear-gradient(135deg,#e6c53a,#3a7bd0 60%,#1c3a6a)}
  .photo.map{left:190px;background:linear-gradient(160deg,#ffffff 40%,#f4a93a)}
  .photo.cigars{left:343px;background:linear-gradient(120deg,#a5623a,#6b3a1f 60%,#3d2211)}
  .story{position:absolute;left:36px;top:164px;width:451px;font-size:10.4px;line-height:14px;text-align:justify}
  .details{position:absolute;left:0;top:365px;width:523px;height:294px;background:var(--back-deep)}
  .col{position:absolute;top:10px;font-size:12px;line-height:15px}
  .col.cost{left:36px}
  .col.included{left:272px;width:220px}
  .col h3{font-family:"Raleway",sans-serif;font-weight:600;font-size:13px;color:var(--coral);line-height:20px}
  .col ul{list-style:none}
  .col li{padding-left:12px;position:relative}
  .col li::before{content:"»";position:absolute;left:0}
  .cost ul{margin-top:16px}
  .cost li{margin-bottom:11px}
  .included li{margin-bottom:4px}
  .notice{position:absolute;left:36px;top:213px;width:451px;height:54px;border:1px solid var(--rule);
    display:grid;grid-template-columns:1fr 175px;align-content:center;row-gap:5px;padding-left:10px;font-family:"Raleway",sans-serif;font-size:12.5px}
  .notice span{display:flex;align-items:center;gap:6px}
  .notice svg{flex:none}
  .footer{position:absolute;left:0;top:676px;width:523px;height:36px;background:var(--footer);display:flex;align-items:center;justify-content:center;gap:8px;
    font-family:"Raleway",sans-serif;font-weight:600;font-size:17px;color:var(--blue-text)}
</style>
</head>
<body>
<div class="canvas">

  <section class="card front" aria-label="Flyer front">
    <div class="hero-photo" role="img" aria-label="Photo of a straw fedora, smoking cigars and a glass of rum on ice over dark smoke"></div>
    <div class="edge-photo" role="img" aria-label="Dark smoke backdrop"></div>

    <div class="panel">
      <div class="panel-inner">
        <div class="event-name">
          <span class="dot"></span>
          <span class="name">Caribe<br>Getaways</span>
        </div>
        <p class="headline">A CUBA CIGAR GENTLEMEN</p>
        <p class="script">Memorial Day Weekend</p>
        <p class="teaser">Cigars, Rum, &amp; Classic Cars...</p>
        <p class="pitch">Legally travel<br>to Cuba and return with real<br><strong>CUBAN CIGARS!</strong></p>
        <div class="band band-year">
          <p class="small">RUM CIGARS AND CLASSIC CARS<br><b>MEMORIAL DAY WEEKEND</b></p>
          <span class="year">2018</span>
        </div>
        <p class="dates-block"><span class="label">DATES:</span><br>Friday, May 25th<br>TO<br>Tuesday May 29th</p>
        <div class="band band-book">
          <p class="cta">BOOK NOW!</p>
          <p class="sub">Space is Limited</p>
        </div>
      </div>
    </div>

    <div class="brand">Lumen<br>Travel</div>
    <p class="contact-front">
      <span class="label">Book Today at</span> <span class="url">www.lumentravel.com/cuba2018</span><br>
      For More Information Call: <span class="phone">XXX-XXX-XXXX</span>
    </p>
  </section>

  <section class="card back" aria-label="Flyer back">
    <div class="photo cars" role="img" aria-label="Photo of colourful classic American cars"></div>
    <div class="photo map" role="img" aria-label="Map of the route from Miami to Havana, Cuba"></div>
    <div class="photo cigars" role="img" aria-label="Close-up photo of Cuban cigars"></div>

    <p class="story">Cuba is the ultimate bucket list destination for any cigar lover. Now is your opportunity to legally travel to Cuba and experience a country that has been off limits to Americans for more than 50 years before it changes. Smoke fine Cuban cigars, meet its resilient people and experience Cuba's fascinating culture. Tour cigar factories, watch expert cigar rollers, visit a humidor factory and work-shop, tour the Old Harbor Rum Museum to learn firsthand the process of making rum followed by rum tasting and pairings with Cuban cigars in a private setting and much more. Explore the Pinar Del Rio located in the Viñales Valley known for its stunning land-scapes and tobacco plantations. Visit the famous Valle Verde Tobacco Plantation to see first hand where and how the tobacco process is grown for fine Cuban Cigars. The bucket list trip of a lifetime awaits on this 'people to people' Cigar Journey to Cuba to learn first hand about Cuban cigars, meet the Cuban people, experience incredible cuisine, drive in classic American cars along the Malecon and experience the Cuban cigar process from 'seed to smoke' and an opportunity to smoke in the birthplace of cigars!</p>

    <div class="details">
      <div class="col cost">
        <h3>Trip Cost : $2050</h3>
        <h3>Deposit : $300</h3>
        <ul>
          <li>Payment plans available</li>
          <li>$300 Deposit Required</li>
          <li>Final payment Due By April 10, 2018</li>
          <li>*NON-REFUNDABLE</li>
          <li>*Passport Required</li>
        </ul>
      </div>
      <div class="col included">
        <h3>What's Included:</h3>
        <ul>
          <li>4 Days / 3 Nights</li>
          <li>5 Star Hotel Accommodations Based on Double Occupancy</li>
          <li>Roundtrip Coastline Airways Tickets from Fort Lauderdale Florida - Cuba</li>
          <li>Tour Bus Chauffeured Transportation</li>
          <li>All Rum and Cigar Tour Events</li>
          <li>Select Meals (Breakfast, Welcome and Farewell Dinner) and More!</li>
        </ul>
      </div>
      <div class="notice">
        <span><svg width="13" height="13" viewBox="0 0 13 13"><rect x="1" y="2" width="10" height="10" fill="none" stroke="#f07c7a" stroke-width="1.4"/><path d="M3.5 7l2.5 2.5L12 2" fill="none" stroke="#f07c7a" stroke-width="1.6"/></svg>$300 Deposit Required</span>
        <span><svg width="13" height="13" viewBox="0 0 13 13"><rect x="1" y="2" width="10" height="10" fill="none" stroke="#f07c7a" stroke-width="1.4"/><path d="M3.5 7l2.5 2.5L12 2" fill="none" stroke="#f07c7a" stroke-width="1.6"/></svg>NON-REFUNDABLE</span>
        <span><svg width="13" height="13" viewBox="0 0 13 13"><rect x="1" y="2" width="10" height="10" fill="none" stroke="#f07c7a" stroke-width="1.4"/><path d="M3.5 7l2.5 2.5L12 2" fill="none" stroke="#f07c7a" stroke-width="1.6"/></svg>Final payment Due By April 10, 2018</span>
        <span><svg width="13" height="13" viewBox="0 0 13 13"><rect x="1" y="2" width="10" height="10" fill="none" stroke="#f07c7a" stroke-width="1.4"/><path d="M3.5 7l2.5 2.5L12 2" fill="none" stroke="#f07c7a" stroke-width="1.6"/></svg>Passport Required</span>
      </div>
    </div>

    <div class="footer">
      <span>For More Information Call:</span>
      <svg width="18" height="18" viewBox="0 0 18 18" aria-hidden="true"><rect x="2" y="3" width="14" height="13" rx="2" fill="none" stroke="#7fb6ee" stroke-width="1.6"/><rect x="4" y="1" width="10" height="4" rx="1.5" fill="#7fb6ee"/><g fill="#7fb6ee"><rect x="5" y="8" width="2" height="2"/><rect x="8" y="8" width="2" height="2"/><rect x="11" y="8" width="2" height="2"/><rect x="5" y="11" width="2" height="2"/><rect x="8" y="11" width="2" height="2"/><rect x="11" y="11" width="2" height="2"/></g></svg>
      <span>XXX-XXX-XXXX</span>
    </div>
  </section>

</div>
</body>
</html>
```